Redesign our business card for more impact

We want to completely replace the back design of our card, and refresh or even change the front entirely. We are happy with our black Q7 logo and do not want to change it.
Our company address changed too. It is now 58 Corvallen, Irvine, CA 92741
Updates

It was reported by Sketch Harbor email today that the uploaded files didnt upload. I am trying again.

Target Market(s)

Architects and Building Owners (People making multi-million dollar decisions)

Industry/Entity Type

Consulting Engineering

Contact Information for Business Card

Contact info on the front. "wallpaper" design on back with tag line on the back "Engineering Your Future"

Font styles to use
Sans Serif

Requirements
Must have
• A vivid, modern, impactful ...but tasteful back of card design. It should communicate our premier status, but grab attention as innovative. DESIGN SHOULD BE ELEGANT AND NOT TOO BUSY.
Nice to have
• Repeating pattern, multi-color, something creative...
Should not have
• Anything that looks too playful or that we are not serious professionals. It should also not be too boring or conservative.

```html
<!DOCTYPE html>
<html lang="en">
<head>
<meta charset="utf-8">
<title>Q7 Business Card</title>
<link rel="stylesheet" href="https://fonts.googleapis.com/css2?family=Montserrat:wght@400;500;700;800&display=swap">
<style>
  :root {
    --stage: #d9d9d7;
    --card: #0b0b0c;
    --card-tone: #141416;
    --ink: #f2f2f2;
    --accent: #d0202a;
  }
  * { margin: 0; padding: 0; box-sizing: border-box; }
  html, body {
    width: 1200px;
    height: 800px;
    overflow: hidden;
  }
  body {
    background: var(--stage);
    font-family: "Montserrat", sans-serif;
    color: var(--ink);
  }
  .sheet {
    width: 1200px;
    height: 800px;
    display: flex;
    align-items: center;
    justify-content: center;
    gap: 60px;
  }
  .card {
    position: relative;
    width: 520px;
    height: 297px;
    background: var(--card);
    box-shadow: 0 10px 24px rgba(0,0,0,0.25);
    overflow: hidden;
  }
  .card__wallpaper {
    position: absolute;
    inset: 0;
    background: linear-gradient(135deg, var(--card) 0%, var(--card-tone) 50%, var(--card) 100%);
  }
  .brand {
    position: absolute;
    font-weight: 800;
    color: var(--ink);
    line-height: 1;
    letter-spacing: -1px;
  }
  /* Back of card */
  .card--back .brand {
    left: 340px;
    top: 112px;
    font-size: 60px;
  }
  .tagline {
    position: absolute;
    left: 318px;
    top: 190px;
    font-size: 10.5px;
    font-weight: 500;
    letter-spacing: 1px;
    text-transform: uppercase;
  }
  /* Front of card */
  .card--front .brand {
    left: 48px;
    top: 52px;
    font-size: 54px;
  }
  .accent-bar {
    position: absolute;
    background: var(--accent);
  }
  .accent-bar--name {
    left: 30px;
    top: 220px;
    width: 3px;
    height: 60px;
  }
  .accent-bar--divider {
    left: 268px;
    top: 150px;
    width: 2px;
    height: 110px;
  }
  .person {
    position: absolute;
    left: 48px;
    top: 205px;
  }
  .person__name {
    font-size: 16px;
    font-weight: 700;
    color: var(--accent);
    text-transform: uppercase;
    margin-bottom: 4px;
  }
  .person__line {
    font-size: 12px;
    font-weight: 400;
    line-height: 1.35;
  }
  .contact {
    position: absolute;
    left: 288px;
    top: 160px;
    list-style: none;
  }
  .contact__item {
    display: flex;
    align-items: center;
    gap: 7px;
    font-size: 12px;
    font-weight: 400;
    margin-bottom: 9px;
  }
  .contact__icon {
    width: 13px;
    height: 13px;
    flex: none;
  }
</style>
</head>
<body>
  <main class="sheet">
    <section class="card card--back" aria-label="Card back">
      <div class="card__wallpaper" role="img" aria-label="Faint repeating brand wallpaper pattern"></div>
      <div class="brand">Q7</div>
      <p class="tagline">Engineering Your Future</p>
    </section>

    <section class="card card--front" aria-label="Card front">
      <div class="card__wallpaper" role="img" aria-label="Faint repeating brand wallpaper pattern"></div>
      <div class="brand">Q7</div>

      <span class="accent-bar accent-bar--name"></span>
      <div class="person">
        <p class="person__name">Dorian Keller, PE</p>
        <p class="person__line">HFDP, LEED AP</p>
        <p class="person__line">CEO/Principal</p>
      </div>

      <span class="accent-bar accent-bar--divider"></span>
      <ul class="contact">
        <li class="contact__item">
          <svg class="contact__icon" viewBox="0 0 14 14" aria-hidden="true"><circle cx="7" cy="7" r="7" fill="#d0202a"/><path d="M7 3.2a2.4 2.4 0 0 0-2.4 2.4c0 1.8 2.4 4.6 2.4 4.6s2.4-2.8 2.4-4.6A2.4 2.4 0 0 0 7 3.2zm0 3.3a.9.9 0 1 1 0-1.8.9.9 0 0 1 0 1.8z" fill="#0b0b0c"/></svg>
          58 Corvallen, Irvine, CA 92741
        </li>
        <li class="contact__item">
          <svg class="contact__icon" viewBox="0 0 14 14" aria-hidden="true"><circle cx="7" cy="7" r="7" fill="#d0202a"/><path d="M4.6 3.8l1.3-.2.7 1.7-.8.6c.4.9 1.1 1.6 2 2l.6-.8 1.7.7-.2 1.3c-3 .3-5.6-2.3-5.3-5.3z" fill="#0b0b0c"/></svg>
          (626) 555-0147
        </li>
        <li class="contact__item">
          <svg class="contact__icon" viewBox="0 0 14 14" aria-hidden="true"><circle cx="7" cy="7" r="7" fill="#d0202a"/><rect x="3.6" y="4.6" width="6.8" height="4.8" fill="#0b0b0c"/><path d="M3.6 4.6L7 7.3l3.4-2.7" stroke="#d0202a" stroke-width="0.8" fill="none"/></svg>
          dorian.keller@q7eng.com
        </li>
        <li class="contact__item">
          <svg class="contact__icon" viewBox="0 0 14 14" aria-hidden="true"><circle cx="7" cy="7" r="7" fill="#d0202a"/><g fill="none" stroke="#0b0b0c" stroke-width="0.9"><circle cx="7" cy="7" r="3.6"/><ellipse cx="7" cy="7" rx="1.5" ry="3.6"/><path d="M3.4 7h7.2"/></g></svg>
          q7eng.com
        </li>
      </ul>
    </section>
  </main>
</body>
</html>
```